Accounting firm needs a postcard design

We need a postcard design for our accounting office for a advertising campaign mailing we do yearly from a mail list we create. We are a full-service accounting office that has been in business for 35 years. I have attached our logo in different formats along with a document with a description of the services we provide. I have also attached my business card and the business card of our CPA. The business cards will have contact information for the postcard design. The contact email that will need to be on the postcard is contact@marlowtaxpartners.com.

```html
<!DOCTYPE html>
<html lang="en">
<head>
<meta charset="utf-8">
<title>Marlow Tax Partners – Postcard</title>
<link rel="stylesheet" href="https://fonts.googleapis.com/css2?family=Montserrat:wght@400;500;600;700;800&display=swap">
<style>
  :root{
    --page:#bebdbe;
    --navy:#0f1d4f;
    --navy-deep:#0a1440;
    --navy-soft:#1d3070;
    --green:#3b8a1f;
    --green-dark:#1f5c0c;
    --green-icon:#5fbf3a;
    --sky:#3da3ea;
    --ink:#141414;
    --white:#ffffff;
    --rule:#c8cbd6;
    --address:#9a9ea8;
  }
  *{box-sizing:border-box;margin:0;padding:0}
  html,body{width:800px;height:1200px;overflow:hidden}
  body{background:var(--page);font-family:'Montserrat',sans-serif;position:relative}

  .postcard{position:absolute;left:30px;width:740px;height:494px;overflow:hidden;background:var(--white);box-shadow:0 6px 18px rgba(0,0,0,.18)}
  .postcard--front{top:52px}
  .postcard--back{top:628px}

  /* front */
  .front-hero{position:absolute;left:0;top:0;width:740px;height:399px;
    background:radial-gradient(ellipse at 50% 70%,var(--navy-soft) 0%,var(--navy) 45%,var(--navy-deep) 100%)}
  .logo-tab{position:absolute;left:261px;top:0;width:218px;height:125px;background:var(--white);border-radius:0 0 12px 12px;
    display:flex;flex-direction:column;align-items:center;justify-content:center;gap:10px}
  .logo-dot{width:34px;height:34px;border-radius:50%;background:var(--green)}
  .logo-name{font-weight:700;color:var(--navy);font-size:12px;letter-spacing:.8px}
  .headline{position:absolute;left:0;right:0;top:180px;text-align:center;color:var(--white);font-weight:400;font-size:24px;line-height:39px;letter-spacing:.2px}
  .headline strong{display:block;color:var(--sky);font-weight:800;font-size:30px;margin-top:4px}
  .experience-pill{position:absolute;left:202px;top:354px;width:336px;height:59px;border-radius:12px;
    background:linear-gradient(180deg,var(--green) 0%,var(--green-dark) 100%);
    color:var(--white);font-weight:800;font-size:25px;display:flex;align-items:center;justify-content:center;letter-spacing:.3px}
  .front-url{position:absolute;left:0;right:0;top:430px;text-align:center;font-weight:700;font-size:21px;color:var(--ink)}

  /* back */
  .services-panel{position:absolute;left:0;top:0;width:405px;height:494px;
    background:radial-gradient(ellipse at 40% 55%,var(--navy-soft) 0%,var(--navy) 55%,var(--navy-deep) 100%)}
  .services-tab{position:absolute;left:23px;top:0;width:272px;height:41px;background:var(--green);border-radius:0 0 12px 12px;
    color:var(--white);font-weight:600;font-size:16px;display:flex;align-items:center;padding-left:23px;letter-spacing:.3px}
  .service{position:absolute;left:25px;width:345px;color:var(--white)}
  .service-head{display:flex;align-items:center;gap:10px;height:26px;border-bottom:1px solid rgba(255,255,255,.55);width:322px;padding-bottom:3px}
  .service-head svg{flex:none}
  .service-title{font-size:13px;font-weight:400;letter-spacing:.2px}
  .service-text{font-size:9.2px;line-height:12.4px;margin-top:7px;width:340px}
  .service--tax{top:64px}
  .service--books{top:161px}
  .service--reports{top:280px}
  .service--payroll{top:377px}

  .mail-side{position:absolute;left:405px;top:0;width:335px;height:494px}
  .mini-logo{position:absolute;left:64px;top:86px;width:120px;display:flex;flex-direction:column;align-items:center;gap:6px}
  .mini-logo .logo-dot{width:20px;height:20px}
  .mini-logo .logo-name{font-size:7px;letter-spacing:.4px}
  .stamp-box{position:absolute;left:195px;top:77px;width:82px;height:81px;border:1px solid var(--rule)}
  .address-line{position:absolute;left:73px;width:204px;height:1px;background:var(--address)}
  .address-line--1{top:185px}
  .address-line--2{top:210px}
  .address-line--3{top:234px}
  .contact{position:absolute;left:99px;top:380px;color:var(--ink)}
  .contact-row{display:flex;align-items:center;gap:12px}
  .contact-row svg{flex:none}
  .contact-phone{font-weight:700;font-size:23px}
  .contact-small{font-size:11px;margin-top:8px}
</style>
</head>
<body>

<section class="postcard postcard--front" aria-label="Postcard front">
  <div class="front-hero" role="img" aria-label="Dark navy photo of cupped hands protecting a young plant growing from coins"></div>
  <div class="logo-tab">
    <span class="logo-dot"></span>
    <span class="logo-name">MARLOW TAX PARTNERS</span>
  </div>
  <h1 class="headline">INDIVIDUALIZED BUSINESS &amp;<br>PERSONAL ACCOUNTING SERVICES<strong>YOU CAN TRUST.</strong></h1>
  <div class="experience-pill">35 YEARS EXPERIENCE</div>
  <p class="front-url">www.marlowtaxpartners.com</p>
</section>

<section class="postcard postcard--back" aria-label="Postcard back">
  <div class="services-panel" role="img" aria-label="Navy background with a faint photo of a plant and coins"></div>
  <div class="services-tab">SERVICES WE PROVIDE</div>

  <article class="service service--tax">
    <div class="service-head">
      <svg width="24" height="24" viewBox="0 0 24 24" fill="none" stroke="var(--green-icon)" stroke-width="1.4"><path d="M6 3h9l4 4v14H6z"/><path d="M15 3v4h4"/><path d="M9 12h7M9 15h7M9 18h4"/></svg>
      <span class="service-title">TAX PREPARATION</span>
    </div>
    <p class="service-text">With over 35 years of experience filing tax returns, we are experts in tax preparation. Including Personal Returns, Corporations, LLC's, Partnerships and State Franchise Tax Returns.</p>
  </article>

  <article class="service service--books">
    <div class="service-head">
      <svg width="24" height="24" viewBox="0 0 24 24" fill="none" stroke="var(--green-icon)" stroke-width="1.4"><rect x="4" y="3" width="11" height="18" rx="1"/><rect x="6" y="5" width="7" height="4"/><path d="M7 12h1M10 12h1M7 15h1M10 15h1M7 18h1M10 18h1"/><rect x="15" y="9" width="6" height="12"/></svg>
      <span class="service-title">BOOKKEEPING</span>
    </div>
    <p class="service-text">Let us take over the day-to-day bookkeeping so you can get back to running your business. We offer assistance with LedgerDesk setup and provide ongoing bookkeeping services. Including frequent journal entries, accounts payables &amp; receivables, sales tax reporting &amp; payments, account reconciliation, and more.</p>
  </article>

  <article class="service service--reports">
    <div class="service-head">
      <svg width="24" height="24" viewBox="0 0 24 24" fill="none" stroke="var(--green-icon)" stroke-width="1.4"><rect x="3" y="4" width="11" height="14"/><path d="M6 8h5M6 11h5"/><path d="M14 20v-5M17 20v-8M20 20v-11M13 20h8"/></svg>
      <span class="service-title">FINANCIAL REPORTING</span>
    </div>
    <p class="service-text">We'll provide easy to understand financial reports that allow you and your team to manage cash flow, create budgets and make forecasting decisions. Depending on your needs, we can provide monthly, quarterly or yearly financial statements.</p>
  </article>

  <article class="service service--payroll">
    <div class="service-head">
      <svg width="24" height="24" viewBox="0 0 24 24" fill="none" stroke="var(--green-icon)" stroke-width="1.4"><circle cx="18" cy="6" r="3"/><path d="M4 10a8 8 0 0 1 9-6M20 14a8 8 0 0 1-9 6"/><rect x="8" y="11" width="8" height="7"/><path d="M10 11V9h4v2"/></svg>
      <span class="service-title">PAYROLL PROCESSING</span>
    </div>
    <p class="service-text">Whether you have 5 employees or 100+, payroll can be an overwhelming and time consuming task. We offer full-service payroll processing. Including employee onboarding, printed or direct deposit checks, quarterly payroll report filing, yearly W-2/W-3 and 1099 printing and filing, and more.</p>
  </article>

  <div class="mail-side">
    <div class="mini-logo">
      <span class="logo-dot"></span>
      <span class="logo-name">MARLOW TAX PARTNERS</span>
    </div>
    <div class="stamp-box"></div>
    <span class="address-line address-line--1"></span>
    <span class="address-line address-line--2"></span>
    <span class="address-line address-line--3"></span>

    <div class="contact">
      <div class="contact-row">
        <svg width="18" height="18" viewBox="0 0 18 18"><circle cx="9" cy="9" r="9" fill="#3b8a1f"/><path d="M6 4.5l1.6 2.2-1 1.1a6 6 0 0 0 3.6 3.6l1.1-1 2.2 1.6-.9 1.6c-3.8-.2-7-3.4-7.2-7.2z" fill="#fff"/></svg>
        <span class="contact-phone">(555)214-7360</span>
      </div>
      <div class="contact-row contact-small">
        <svg width="18" height="14" viewBox="0 0 18 14"><rect width="18" height="14" fill="#0f1d4f"/><path d="M1 1l8 7 8-7M1 13l6-6M17 13l-6-6" stroke="#fff" stroke-width="1.3" fill="none"/></svg>
        <span>contact@marlowtaxpartners.com</span>
      </div>
      <div class="contact-row contact-small">
        <svg width="18" height="18" viewBox="0 0 18 18" fill="none" stroke="#0f1d4f" stroke-width="1.4"><circle cx="9" cy="9" r="8"/><ellipse cx="9" cy="9" rx="3.5" ry="8"/><path d="M1 9h16M2.5 5h13M2.5 13h13"/></svg>
        <span>marlowtaxpartners.com</span>
      </div>
    </div>
  </div>
</section>

</body>
</html>
```